Moder Business Card Design for Renewables Business

Need a business card design for my business. We collect & repurpose spent coffee ground from cafes. The cards will be made from recycled paper. Needs to fit our corporate colour scheme of white, green & brown (see logo for colour codes). Eco friendly, modern, intresting & eye catching.
This card needs to convey the message of the business and fit into its mantra of eco-friendly, sustainable etc.

Target Market(s)

Cafe Owners, Coffee Drinkers, Recycling Companies, Farmers

Industry/Entity Type

Recycling

Contact Information for Business Card

Name; Peter Dalton
Phone; 0438 216 570
e-mail; info@florivex.com.au
website; www.florivex.com.au

Font styles to use
Sans Serif
Script

Colors

Designer to choose colors to be used in the design.

Requirements
Must have
• FRONT;
• Logo, Name (Peter Dalton), phone number, e-mail address, website
• BACK;
• On the back in cursive text; 'GIVING SPENT COFFEE A SECOND LIFE'
• Small facebook & Instagram logos with text 'Florivex'
Should not have
• messy design

```html
<!DOCTYPE html>
<html lang="en">
<head>
<meta charset="utf-8">
<title>Florivex Business Card</title>
<link href="https://fonts.googleapis.com/css2?family=Josefin+Sans:wght@400;600&display=swap" rel="stylesheet">
<style>
  :root {
    --backdrop: #2b2b2e;
    --kraft: #b38d64;
    --kraft-light: #bf9a72;
    --kraft-dark: #a47d55;
    --green: #5d8a35;
    --leaf-dark: #3f6b22;
    --brown: #3e2a1f;
    --brown-soft: #5a4030;
  }
  * { box-sizing: border-box; margin: 0; padding: 0; }
  html, body { width: 1200px; height: 800px; overflow: hidden; }
  body {
    background: var(--backdrop);
    font-family: "Josefin Sans", sans-serif;
    display: flex;
    align-items: center;
    justify-content: center;
    gap: 50px;
  }
  .card {
    position: relative;
    width: 525px;
    height: 300px;
    background:
      radial-gradient(circle at 30% 20%, var(--kraft-light), transparent 60%),
      radial-gradient(circle at 80% 90%, var(--kraft-dark), transparent 55%),
      var(--kraft);
    overflow: hidden;
    box-shadow: 0 6px 18px rgba(0,0,0,0.35);
  }

  /* Front */
  .brand {
    position: absolute;
    right: 52px;
    top: 56px;
    display: flex;
    flex-direction: column;
    align-items: center;
    gap: 14px;
  }
  .brand-mark {
    width: 96px;
    height: 96px;
    border: 4px solid var(--brown);
    border-radius: 50%;
  }
  .brand-name {
    font-weight: 600;
    font-size: 22px;
    letter-spacing: 2px;
    color: var(--green);
  }
  .contact {
    position: absolute;
    left: 40px;
    bottom: 38px;
  }
  .contact-name {
    font-size: 24px;
    letter-spacing: 1px;
    color: var(--brown-soft);
    margin-bottom: 10px;
  }
  .contact-name .first { color: var(--green); }
  .contact-row {
    display: flex;
    align-items: center;
    gap: 10px;
    font-size: 13px;
    letter-spacing: 1px;
    color: var(--brown);
    line-height: 1;
    margin-top: 5px;
  }
  .contact-key {
    width: 15px;
    height: 15px;
    background: var(--brown);
    color: var(--kraft-light);
    font-size: 10px;
    display: flex;
    align-items: center;
    justify-content: center;
    padding-top: 2px;
  }

  /* Back */
  .tagline {
    position: absolute;
    top: 92px;
    width: 100%;
    text-align: center;
    font-size: 19px;
    letter-spacing: 2px;
    color: var(--brown);
  }
  .social {
    position: absolute;
    top: 128px;
    width: 100%;
    display: flex;
    justify-content: center;
    align-items: center;
    gap: 10px;
    font-size: 12px;
    letter-spacing: 2px;
    color: var(--brown);
  }
  .social-dot {
    width: 14px;
    height: 14px;
    border-radius: 50%;
    background: var(--green);
  }
  .leaf-spray {
    position: absolute;
    left: 60px;
    right: 60px;
    bottom: -20px;
    height: 130px;
    background: radial-gradient(ellipse at 55% 70%, var(--leaf-dark) 0%, var(--green) 40%, rgba(93,138,53,0.35) 65%, transparent 78%);
  }
</style>
</head>
<body>
  <section class="card card-front">
    <div class="brand">
      <div class="brand-mark"></div>
      <div class="brand-name">FLORIVEX</div>
    </div>
    <div class="contact">
      <p class="contact-name"><span class="first">PETER</span> DALTON</p>
      <div class="contact-row"><span class="contact-key">P</span>0438 216 570</div>
      <div class="contact-row"><span class="contact-key">E</span>info@florivex.com.au</div>
      <div class="contact-row"><span class="contact-key">W</span>www.florivex.com.au</div>
    </div>
  </section>

  <section class="card card-back">
    <p class="tagline">GIVING SPENT COFFEE A SECOND LIFE</p>
    <div class="social">
      <span class="social-dot"></span>
      <span>Florivex</span>
    </div>
    <div class="leaf-spray" role="img" aria-label="Cluster of fresh green leaves rising from the bottom edge"></div>
  </section>
</body>
</html>
```